Construction Company Business Card

Business Card Design using new Logo

Contact Information for Business Card

include all company info and website

Requirements
Must have
• Wesley Corman - President
ph. 254-617-0382
Cedar Knoll, TX
wesley@ironmarkframing.com
www.ironmarkframing.com

```html
<!DOCTYPE html>
<html lang="en">
<head>
<meta charset="utf-8">
<title>Ironmark Framing Texas – Business Card</title>
<link href="https://fonts.googleapis.com/css2?family=Montserrat:wght@500;600&family=Roboto:wght@400;700&display=swap" rel="stylesheet">
<style>
  :root {
    --backdrop: #4a0a18;
    --card: #171717;
    --card-edge: #262626;
    --red: #c8202c;
    --white: #f2f2f2;
    --grey: #c9c9c9;
    --emboss: #3a3a3a;
  }
  * { margin: 0; padding: 0; box-sizing: border-box; }
  html, body { width: 1200px; height: 900px; overflow: hidden; }
  body {
    background: var(--backdrop);
    font-family: "Roboto", Arial, sans-serif;
    position: relative;
  }
  .card {
    position: absolute;
    left: 337px;
    width: 525px;
    height: 300px;
    background: var(--card);
    border: 1px solid var(--card-edge);
    box-shadow: 0 18px 40px rgba(0,0,0,.45);
  }
  .card--back { top: 100px; }
  .card--front { top: 470px; }

  /* Back */
  .back-wordmark {
    position: absolute;
    top: 92px; left: 0; right: 0;
    text-align: center;
    font-family: "Montserrat", Arial, sans-serif;
    font-weight: 600;
    font-size: 34px;
    letter-spacing: 2px;
    color: var(--emboss);
  }
  .back-tagline {
    position: absolute;
    top: 228px; left: 0; right: 0;
    text-align: center;
    font-family: "Montserrat", Arial, sans-serif;
    font-weight: 500;
    font-size: 10px;
    letter-spacing: 5px;
    color: var(--white);
  }

  /* Front */
  .brand {
    position: absolute;
    top: 52px; left: 0; right: 0;
    display: flex;
    justify-content: center;
    align-items: center;
    gap: 10px;
  }
  .brand__dot {
    width: 12px; height: 12px;
    border-radius: 50%;
    background: var(--red);
  }
  .brand__name {
    font-family: "Montserrat", Arial, sans-serif;
    font-weight: 600;
    font-size: 24px;
    letter-spacing: 1.5px;
    color: var(--white);
  }
  .brand-rule {
    position: absolute;
    top: 98px; left: 110px; right: 110px;
    height: 1px;
    background: var(--red);
  }
  .person {
    position: absolute;
    left: 52px; top: 198px;
  }
  .person__name {
    font-weight: 700;
    font-size: 20px;
    color: var(--grey);
  }
  .person__title {
    font-weight: 700;
    font-size: 14px;
    color: var(--red);
    margin-top: 2px;
  }
  .divider {
    position: absolute;
    left: 250px; top: 150px;
    width: 1px; height: 110px;
    background: var(--red);
  }
  .contacts {
    position: absolute;
    left: 270px; top: 152px;
    list-style: none;
  }
  .contacts li {
    display: flex;
    align-items: center;
    gap: 10px;
    height: 26px;
    font-size: 12px;
    color: var(--white);
    letter-spacing: .3px;
  }
  .contacts svg { width: 16px; height: 16px; flex: none; }
</style>
</head>
<body>

<section class="card card--back">
  <div class="back-wordmark">IRONMARK FRAMING</div>
  <div class="back-tagline">IRONMARK FRAMING TEXAS</div>
</section>

<section class="card card--front">
  <div class="brand">
    <span class="brand__dot"></span>
    <span class="brand__name">IRONMARK FRAMING</span>
  </div>
  <div class="brand-rule"></div>

  <div class="person">
    <div class="person__name">Wesley Corman</div>
    <div class="person__title">President</div>
  </div>

  <div class="divider"></div>

  <ul class="contacts">
    <li>
      <svg viewBox="0 0 16 16"><circle cx="8" cy="8" r="8" fill="#c8202c"/><path d="M5 4.5c.6-.5 1.1-.3 1.4.3l.5 1c.2.4 0 .8-.3 1l-.4.3c.4.9 1.1 1.6 2 2l.3-.4c.3-.3.6-.4 1-.3l1 .5c.6.3.8.8.3 1.4-.7.9-1.6 1-2.6.5-1.5-.7-2.7-1.9-3.4-3.4-.5-1-.4-1.9.2-2.9z" fill="#171717"/></svg>
      254-617-0382
    </li>
    <li>
      <svg viewBox="0 0 16 16"><circle cx="8" cy="8" r="8" fill="#c8202c"/><path d="M8 3.8a2.8 2.8 0 0 0-2.8 2.8C5.2 8.7 8 12 8 12s2.8-3.3 2.8-5.4A2.8 2.8 0 0 0 8 3.8z" fill="#171717"/><circle cx="8" cy="6.6" r="1" fill="#c8202c"/></svg>
      Cedar Knoll, TX
    </li>
    <li>
      <svg viewBox="0 0 16 16"><circle cx="8" cy="8" r="8" fill="#c8202c"/><text x="8" y="11.2" text-anchor="middle" font-size="9" font-family="Roboto, Arial, sans-serif" font-weight="700" fill="#171717">@</text></svg>
      wesley@ironmarkframing.com
    </li>
    <li>
      <svg viewBox="0 0 16 16"><circle cx="8" cy="8" r="8" fill="#c8202c"/><g fill="none" stroke="#171717" stroke-width=".9"><circle cx="8" cy="8" r="4"/><ellipse cx="8" cy="8" rx="1.7" ry="4"/><path d="M4 8h8"/></g></svg>
      www.ironmarkframing.com
    </li>
  </ul>
</section>

</body>
</html>
```